Bakery Business Cards

We are in need of business cards for our bakery business--something non-generic that reflects our business and will stand out. We are a wholesale bakery that primarily services in-store bakeries, casinos, schools, distributors, and fund-raising companies. The family business was founded in 1960. (www.marlowsovenworks.com)

```html
<!DOCTYPE html>
<html lang="en">
<head>
<meta charset="utf-8">
<title>Marlow's Ovenworks – Business Card</title>
<link href="https://fonts.googleapis.com/css2?family=Lora:wght@400;600&display=swap" rel="stylesheet">
<style>
  :root{
    --page:#e9e9e9;
    --blue-deep:#063f7e;
    --blue-mid:#0d5fae;
    --blue-light:#1a7bd0;
    --gold:#f2c27e;
    --cream:#fbe3b8;
    --white:#ffffff;
    --photo-warm:#d9a777;
    --photo-berry:#a8343e;
    --photo-plate:#f3efe9;
  }
  html,body{margin:0;padding:0;width:1200px;height:2177px;overflow:hidden;background:var(--page);}
  .canvas{position:relative;width:1200px;height:2177px;}
  .business-card{
    position:absolute;left:100px;top:803px;width:1000px;height:571px;
    box-shadow:0 18px 40px rgba(0,0,0,.22);overflow:hidden;
    font-family:'Lora',Georgia,serif;
  }
  .card-art{position:absolute;inset:0;}
  .brand{
    position:absolute;left:480px;width:460px;top:34px;text-align:center;color:var(--white);
  }
  .brand-name{font-size:44px;font-weight:600;line-height:1.02;margin:0;}
  .brand-since{font-size:18px;font-weight:400;letter-spacing:2px;margin-top:8px;line-height:1;}
  .divider{position:absolute;left:470px;top:192px;width:475px;height:2px;background:var(--white);}
  .contact-list{position:absolute;left:555px;top:232px;margin:0;padding:0;list-style:none;color:var(--gold);font-size:24px;}
  .contact-item{display:flex;align-items:flex-start;margin-bottom:24px;line-height:1.25;}
  .contact-icon{width:26px;height:26px;margin-right:20px;flex:none;margin-top:2px;}
</style>
</head>
<body>
<div class="canvas">
  <article class="business-card">
    <svg class="card-art" viewBox="0 0 1000 571" width="1000" height="571">
      <defs>
        <linearGradient id="photoTone" x1="0" y1="0" x2="1" y2="1">
          <stop offset="0" stop-color="var(--photo-plate)"/>
          <stop offset=".35" stop-color="var(--photo-warm)"/>
          <stop offset=".6" stop-color="var(--photo-berry)"/>
          <stop offset="1" stop-color="var(--photo-warm)"/>
        </linearGradient>
        <linearGradient id="panelBlue" x1="0" y1="0" x2="1" y2="1">
          <stop offset="0" stop-color="var(--blue-deep)"/>
          <stop offset=".45" stop-color="var(--blue-light)"/>
          <stop offset="1" stop-color="var(--blue-deep)"/>
        </linearGradient>
      </defs>
      <rect class="photo-area" x="0" y="0" width="520" height="571" fill="url(#photoTone)" role="img" aria-label="Top-down photo of berry pies and pie slices on white plates"/>
      <path class="stripe-ground" d="M396 0 Q226 200 221 571 L1000 571 L1000 0 Z" fill="var(--blue-mid)"/>
      <path class="blue-panel" d="M488 0 Q323 200 318 571 L1000 571 L1000 0 Z" fill="url(#panelBlue)"/>
      <g class="arc-stripes" fill="none" stroke-width="8">
        <path d="M400 0 Q230 200 225 571" stroke="var(--cream)"/>
        <path d="M422 0 Q252 200 247 571" stroke="var(--gold)"/>
        <path d="M444 0 Q274 200 269 571" stroke="var(--cream)"/>
        <path d="M470 0 Q305 200 300 571" stroke="var(--gold)"/>
      </g>
    </svg>

    <header class="brand">
      <p class="brand-name">Marlow's<br>Ovenworks</p>
      <div class="brand-since">SINCE 1960</div>
    </header>
    <div class="divider"></div>

    <ul class="contact-list">
      <li class="contact-item">
        <svg class="contact-icon" viewBox="0 0 24 24"><path d="M6.6 10.8a15 15 0 0 0 6.6 6.6l2.2-2.2c.3-.3.7-.4 1-.2 1.1.4 2.3.6 3.6.6.6 0 1 .4 1 1V20c0 .6-.4 1-1 1A17 17 0 0 1 3 4c0-.6.4-1 1-1h3.5c.6 0 1 .4 1 1 0 1.3.2 2.5.6 3.6.1.3 0 .7-.2 1z" fill="var(--gold)"/></svg>
        <span>(405)555-0172</span>
      </li>
      <li class="contact-item">
        <svg class="contact-icon" viewBox="0 0 24 24"><circle cx="12" cy="12" r="4" fill="none" stroke="var(--gold)" stroke-width="2.4"/><path d="M16 8v5.5a2.5 2.5 0 0 0 5 0V12a9 9 0 1 0-3.5 7.1" fill="none" stroke="var(--gold)" stroke-width="2.4"/></svg>
        <span>sales@marlowsovenworks.com</span>
      </li>
      <li class="contact-item">
        <svg class="contact-icon" viewBox="0 0 24 24"><path d="M12 3 2 12h3v8h5v-5h4v5h5v-8h3z" fill="var(--gold)"/></svg>
        <span>1187 Harlan Ave,<br>Oklahoma City, OK 73109</span>
      </li>
      <li class="contact-item">
        <svg class="contact-icon" viewBox="0 0 24 24"><g fill="none" stroke="var(--gold)" stroke-width="2"><circle cx="12" cy="12" r="9.5"/><ellipse cx="12" cy="12" rx="4" ry="9.5"/><path d="M2.5 12h19M4 7h16M4 17h16"/></g></svg>
        <span>www.marlowsovenworks.com</span>
      </li>
    </ul>
  </article>
</div>
</body>
</html>
```